Business card revamp

we are refrigeration mechanic i need a modern professional double side business card using my current branding
The card information must have site address~ 17 Pellham st cobram, Vic 3644 postal address~ P.o. Box 862 cobram,Vic 3643 Phone Number~0358941637 Fax Nunber~0358936205 Email address~ brettk@vorlatek.com.au Title~ Manager Licence numbers~ AU47319, NSW 481927D Web site~ www.frostwaylane.com.au

```html
<!DOCTYPE html>
<html lang="en">
<head>
<meta charset="utf-8">
<title>Frostway Lane – Business Card</title>
<link rel="stylesheet" href="https://fonts.googleapis.com/css2?family=Mulish:wght@400;600;700;800&display=swap">
<style>
  :root {
    --backdrop: #e4e4e4;
    --card-light: #ffffff;
    --card-dark: #2a2a2a;
    --card-dark-edge: #1f1f1f;
    --brand-red: #c1272d;
    --brand-blue: #1f6fb5;
    --ink-dark: #2b2b2b;
    --ink-grey: #9a9a9a;
    --ink-light: #f2f2f2;
    --label-red: #d2383d;
  }
  * { box-sizing: border-box; margin: 0; padding: 0; }
  html, body {
    width: 1200px; height: 720px; overflow: hidden;
    background: var(--backdrop);
    font-family: "Mulish", sans-serif;
  }
  .canvas { position: relative; width: 1200px; height: 720px; }
  .card {
    position: absolute; top: 241px;
    width: 420px; height: 240px;
  }
  .card--front { left: 147px; background: var(--card-light); }
  .card--back {
    left: 633px;
    background: linear-gradient(160deg, var(--card-dark) 0%, var(--card-dark-edge) 100%);
    color: var(--ink-light);
  }

  /* front */
  .front-brand {
    position: absolute; left: 0; right: 0; top: 84px;
    text-align: center;
    font-weight: 800; font-size: 34px; letter-spacing: 1px;
    color: var(--brand-red); text-transform: uppercase;
  }
  .front-tagline {
    position: absolute; left: 0; right: 0; top: 131px;
    text-align: center; font-size: 9.5px; letter-spacing: 1.6px;
    color: var(--ink-dark); text-transform: uppercase; font-weight: 600;
  }
  .front-web {
    position: absolute; left: 0; right: 0; top: 206px;
    text-align: center; font-size: 12.5px; font-weight: 700;
    color: var(--ink-dark);
  }

  /* back */
  .back-brand {
    position: absolute; left: 12px; top: 34px;
    font-weight: 800; font-size: 18px; letter-spacing: 0.6px;
    color: var(--brand-red); text-transform: uppercase; line-height: 1;
  }
  .back-tagline {
    position: absolute; left: 40px; top: 55px;
    font-size: 5.5px; letter-spacing: 1px; color: var(--ink-grey);
    text-transform: uppercase; font-weight: 600;
  }
  .licence {
    position: absolute; left: 12px; top: 92px;
    font-size: 11px; font-weight: 700; color: var(--ink-grey); line-height: 15px;
  }
  .person {
    position: absolute; right: 12px; top: 106px; text-align: right;
  }
  .person__name { font-size: 15.5px; font-weight: 700; color: var(--brand-blue); }
  .person__title { font-size: 12px; color: var(--ink-light); margin-top: 3px; }
  .contact {
    position: absolute; left: 12px;
    font-size: 11px; line-height: 14px; white-space: nowrap;
  }
  .contact__label { color: var(--label-red); font-weight: 600; }
  .contact--phone { top: 129px; }
  .contact--email { top: 167px; }
  .contact--address { top: 192px; line-height: 16px; }
</style>
</head>
<body>
<main class="canvas">
  <section class="card card--front" aria-label="Card front">
    <div class="front-brand">Frostway Lane</div>
    <div class="front-tagline">Heating and Cooling Specialists</div>
    <div class="front-web">frostwaylane.com.au</div>
  </section>

  <section class="card card--back" aria-label="Card back">
    <div class="back-brand">Frostway Lane</div>
    <div class="back-tagline">Heating and Cooling Specialists</div>

    <div class="licence">
      <div>Licence # AU47319</div>
      <div>NSW 481927D</div>
    </div>

    <div class="person">
      <div class="person__name">Brett Kalandris</div>
      <div class="person__title">Manager</div>
    </div>

    <div class="contact contact--phone">
      <div><span class="contact__label">Ph:</span> 035.894.1637</div>
      <div><span class="contact__label">Fax:</span> 03.589.36205</div>
    </div>
    <div class="contact contact--email">
      <span class="contact__label">Email:</span> brettk@vorlatek.com.au
    </div>
    <div class="contact contact--address">
      <div><span class="contact__label">Postal Address:</span> P.o. Box 862 cobram,Vic 3643</div>
      <div><span class="contact__label">Site Address:</span> 17 Pellham st cobram, Vic 3644</div>
    </div>
  </section>
</main>
</body>
</html>
```